Kid's Cancer Camp Business Card

Create a unique Two-Sided color business cards for Camp Willow Brook, a pediatric cancer camp.

The camp tag line is: A place where every camper finds joy...

Dale Morrisey, Executive Director
Camp Willow Brook Charitable Foundation, Inc
PO Box 918
Fernhollow, MA 06832

Phone - 203-555-0143
Fax - 203-555-0187
Email: dale@campwillowbrook.example
www.campwillowbrook.example

Target Market(s)

Potential Donors, Volunteers and Campers

Industry/Entity Type

Non-profit pediatric cancer camp

Contact Information for Business Card

All contact info that is included in the description

Font styles to use
Other font styles liked:
• Designer chooses font

Requirements
Must have
• Camp Willow Brook Logo and Tag Line
Nice to have
• should be eye catching
Should not have
• not cartoony

```html
<!DOCTYPE html>
<html lang="en">
<head>
<meta charset="utf-8">
<title>Camp Willow Brook – Business Card</title>
<link href="https://fonts.googleapis.com/css2?family=Open+Sans:wght@400;600;700&display=swap" rel="stylesheet">
<style>
  :root {
    --stage: #2a2a2d;
    --card-dark: #1f1e22;
    --teal: #0aa59c;
    --teal-deep: #078a83;
    --teal-light: #3cc4bb;
    --sun: #f2ad24;
    --ink-light: #ffffff;
  }
  * { box-sizing: border-box; margin: 0; padding: 0; }
  html, body { width: 1200px; height: 780px; overflow: hidden; }
  body {
    background: var(--stage);
    font-family: "Open Sans", Arial, sans-serif;
    position: relative;
  }
  .card {
    position: absolute;
    top: 230px;
    width: 530px;
    height: 320px;
    border-radius: 4px;
    overflow: hidden;
    box-shadow: 0 10px 30px rgba(0,0,0,.45);
  }

  /* Front */
  .card-front { left: 45px; background: var(--card-dark); }
  .front-swoosh { position: absolute; inset: 0; width: 100%; height: 100%; }
  .brand-lockup {
    position: absolute;
    left: 28px;
    top: 48px;
    width: 210px;
    display: flex;
    align-items: center;
    gap: 12px;
  }
  .brand-dot {
    flex: 0 0 44px;
    height: 44px;
    border-radius: 50%;
    background: var(--sun);
  }
  .brand-name {
    color: var(--sun);
    font-weight: 600;
    font-size: 24px;
    line-height: 1.12;
  }
  .contact-block {
    position: absolute;
    left: 262px;
    top: 30px;
    width: 252px;
    color: var(--ink-light);
    font-size: 13px;
    line-height: 1.42;
  }
  .person-name { font-size: 26px; font-weight: 700; line-height: 1.1; white-space: nowrap; }
  .person-name .first { color: var(--sun); }
  .person-name .last { color: var(--teal); }
  .person-title { font-size: 14px; font-weight: 600; margin-bottom: 8px; }
  .address { margin-bottom: 8px; }
  .address .po { color: var(--sun); }
  .contact-list { list-style: none; }
  .contact-list li { display: flex; align-items: center; gap: 7px; white-space: nowrap; }
  .contact-list svg { width: 12px; height: 12px; flex: 0 0 12px; }

  /* Back */
  .card-back { left: 625px; background: var(--teal); }
  .back-pattern {
    position: absolute;
    inset: 0;
    background: linear-gradient(135deg, var(--teal-deep) 0%, var(--teal) 55%, var(--teal-light) 100%);
  }
  .tagline {
    position: absolute;
    left: 30px;
    bottom: 30px;
    color: var(--ink-light);
    font-size: 16px;
  }
  .back-brand {
    position: absolute;
    right: 22px;
    bottom: 32px;
    color: var(--sun);
    font-size: 11px;
    font-weight: 600;
  }
</style>
</head>
<body>

<section class="card card-front" aria-label="Business card front">
  <svg class="front-swoosh" viewBox="0 0 530 320" preserveAspectRatio="none" aria-hidden="true">
    <path d="M0 150 C40 250 95 305 210 320 L0 320 Z" fill="var(--teal)"/>
    <path d="M60 205 C115 270 180 305 262 320 L246 320 C168 306 110 275 60 205 Z" fill="var(--sun)"/>
    <line x1="232" y1="292" x2="252" y2="22" stroke="var(--ink-light)" stroke-width="1.5"/>
  </svg>

  <div class="brand-lockup">
    <span class="brand-dot"></span>
    <span class="brand-name">Camp Willow Brook</span>
  </div>

  <div class="contact-block">
    <h1 class="person-name"><span class="first">Dale</span> <span class="last">Morrisey</span></h1>
    <p class="person-title">Executive Director</p>
    <p class="address">
      Camp Willow Brook Charitable<br>
      Foundation, Inc<br>
      <span class="po">PO Box 918</span><br>
      Fernhollow, MA 06832
    </p>
    <ul class="contact-list">
      <li>
        <svg viewBox="0 0 12 12"><path d="M2 1h3l1 3-1.5 1a6 6 0 0 0 2.5 2.5L8 6l3 1v3c0 .6-.4 1-1 1C5 11 1 7 1 2c0-.6.4-1 1-1z" fill="var(--sun)"/></svg>
        203-555-0143
      </li>
      <li>
        <svg viewBox="0 0 12 12"><rect x="1" y="4" width="10" height="7" rx="1" fill="var(--sun)"/><rect x="3" y="1" width="6" height="4" fill="var(--sun)"/></svg>
        203-555-0187
      </li>
      <li>
        <svg viewBox="0 0 12 12"><circle cx="6" cy="6" r="5" fill="none" stroke="var(--sun)" stroke-width="1.4"/><path d="M1 6h10M6 1c2 2 2 8 0 10M6 1c-2 2-2 8 0 10" fill="none" stroke="var(--sun)" stroke-width="1"/></svg>
        www.campwillowbrook.example
      </li>
      <li>
        <svg viewBox="0 0 12 12"><rect x="1" y="2.5" width="10" height="7" fill="var(--sun)"/><path d="M1 2.5l5 4 5-4" fill="none" stroke="var(--card-dark)" stroke-width="1"/></svg>
        dale@campwillowbrook.example
      </li>
    </ul>
  </div>
</section>

<section class="card card-back" aria-label="Business card back">
  <div class="back-pattern" role="img" aria-label="Repeating pattern of small emblems in darker and lighter teal"></div>
  <p class="tagline">A place where every camper finds joy...</p>
  <span class="back-brand">Camp Willow Brook</span>
</section>

</body>
</html>
```